Tech business card design

We need an amazing business card design for our new business 'Brakka' a marketing tech startup based in Sydney, Australia. We provide an online marketplace for businesses to search and buy advertising media, connect with service providers and learn more about marketing. We wish to communicate 'cool tech', reliability and professionalism and design based around our logo.

Target Market(s)

Business Owners

Contact Information for Business Card

Name
Position
Email Address
Website
Phone Number

Font styles to use
Other font styles liked:
• Avenir & Avenir Next

Colors

Designer to choose colors to be used in the design.

```html
<!DOCTYPE html>
<html lang="en">
<head>
<meta charset="utf-8">
<title>Brakka Business Card</title>
<link rel="stylesheet" href="https://fonts.googleapis.com/css2?family=Nunito+Sans:wght@400;600;800&display=swap">
<style>
  :root {
    --stage: #d9d9d9;
    --card-black: #0e0e0e;
    --card-white: #f4f5f8;
    --ink-navy: #1b1c3a;
    --text-white: #ffffff;
    --text-grey: #b9b9b9;
    --pattern: #1c1c1c;
  }
  * { margin: 0; padding: 0; box-sizing: border-box; }
  html, body { width: 1200px; height: 1000px; overflow: hidden; }
  body {
    background: radial-gradient(ellipse at 50% 40%, #e6e6e6 0%, var(--stage) 55%, #b8b8b8 100%);
    font-family: "Nunito Sans", sans-serif;
    position: relative;
  }
  .card {
    position: absolute;
    width: 640px;
    height: 370px;
    box-shadow: 0 14px 30px rgba(0,0,0,0.28);
    overflow: hidden;
  }
  /* Front */
  .card-front { left: 120px; top: 90px; display: flex; }
  .front-details {
    width: 44%;
    background: var(--card-black);
    color: var(--text-white);
    padding: 96px 0 0 40px;
  }
  .person-name { font-size: 24px; font-weight: 800; line-height: 1; }
  .person-role { font-size: 12px; color: var(--text-grey); margin-top: 4px; }
  .contact-list { list-style: none; margin-top: 28px; }
  .contact-list li {
    display: flex; align-items: center; gap: 16px;
    font-size: 14px; margin-bottom: 20px; color: var(--text-white);
  }
  .contact-list svg { width: 16px; height: 16px; flex: none; }
  .front-brand {
    flex: 1;
    background: var(--card-white);
    display: flex; align-items: center; justify-content: center;
  }
  .wordmark { font-weight: 800; letter-spacing: -1px; line-height: 1; }
  .front-brand .wordmark { font-size: 78px; color: var(--ink-navy); }
  /* Back */
  .card-back {
    left: 400px; top: 530px;
    background: var(--card-black);
    display: flex; flex-direction: column; align-items: center; justify-content: center;
  }
  .back-pattern {
    position: absolute; inset: 0;
    background: linear-gradient(135deg, var(--pattern) 0%, var(--card-black) 60%, var(--pattern) 100%);
  }
  .card-back .wordmark { position: relative; font-size: 110px; color: var(--text-white); }
  .back-url { position: relative; margin-top: 36px; font-size: 18px; color: var(--text-white); }
</style>
</head>
<body>
  <section class="card card-front">
    <div class="front-details">
      <h1 class="person-name">Marcus Dale</h1>
      <p class="person-role">Founder, Director</p>
      <ul class="contact-list">
        <li>
          <svg viewBox="0 0 16 16" aria-hidden="true"><path d="M4 1.5l2.2 3-1.3 1.6a8 8 0 0 0 5 5l1.6-1.3 3 2.2-1.4 2.3C7.6 14.3 1.7 8.4 1.7 2.9z" fill="#fff"/></svg>
          +61 (0)412 555 208
        </li>
        <li>
          <svg viewBox="0 0 16 16" aria-hidden="true"><rect x="1" y="3.5" width="14" height="9" fill="#fff"/><path d="M1 3.5l7 5 7-5" fill="none" stroke="#0e0e0e" stroke-width="1.2"/></svg>
          marcus@brakkamedia.com.au
        </li>
        <li>
          <svg viewBox="0 0 16 16" aria-hidden="true"><circle cx="8" cy="8" r="6.5" fill="none" stroke="#fff" stroke-width="1.3"/><ellipse cx="8" cy="8" rx="2.8" ry="6.5" fill="none" stroke="#fff" stroke-width="1"/><path d="M1.5 8h13" stroke="#fff" stroke-width="1"/></svg>
          www.brakkamedia.com.au
        </li>
      </ul>
    </div>
    <div class="front-brand">
      <span class="wordmark">Brakka</span>
    </div>
  </section>

  <section class="card card-back">
    <div class="back-pattern" role="img" aria-label="Faint repeating brand name pattern across the dark card"></div>
    <span class="wordmark">Brakka</span>
    <p class="back-url">www.brakkamedia.com.au</p>
  </section>
</body>
</html>
```